Business Cards, Letterhead, Corporate Materials

Harlow Building Partners, Inc. needs brand identity and marketing materials.

Target Market(s)

Home Owners, Architects, Engineers.

Contact Information for Business Card

Business Cards for myself the President

Font styles to use
Serif

Colors
3377b5
0255a3
cfdfed
cee9f5
86cae7
0393ce
000000
ffffff
f5f5f5

Requirements
Must have
• My name, my address, my email, phone number, company logo, my title. my contractor's license number, web address.
Nice to have
• Very clean professional modern business cards for company president.

```html
<!DOCTYPE html>
<html lang="en">
<head>
<meta charset="utf-8">
<title>Harlow Building Partners, Inc. — Business Card</title>
<link rel="stylesheet" href="https://fonts.googleapis.com/css2?family=Libre+Baskerville&family=Raleway:wght@400;500&display=swap">
<style>
  :root {
    --stage: #f5f5f5;
    --card-light: #3377b5;
    --card-mid: #0255a3;
    --card-dark: #023f7a;
    --ink: #ffffff;
    --ink-soft: #cee9f5;
    --rule: rgba(207,223,237,0.6);
  }
  * { margin: 0; padding: 0; box-sizing: border-box; }
  html, body { width: 1200px; height: 1022px; overflow: hidden; background: var(--stage); }
  .stage { position: relative; width: 1200px; height: 1022px; }
  .card {
    position: absolute; left: 150px; top: 251px; width: 900px; height: 520px;
    border-radius: 22px;
    background: linear-gradient(135deg, var(--card-light) 0%, var(--card-mid) 50%, var(--card-dark) 100%);
    color: var(--ink);
    box-shadow: 0 14px 40px rgba(2,40,80,0.25);
    overflow: hidden;
  }
  .brand {
    position: absolute; left: 70px; top: 50%; transform: translateY(-50%);
    display: flex; align-items: center; gap: 16px;
    font-family: "Raleway", sans-serif; font-weight: 500; color: var(--ink);
  }
  .brand-mark { width: 62px; height: 62px; background: var(--ink); border-radius: 6px; flex: none; }
  .brand-name { font-size: 25px; line-height: 1.2; letter-spacing: 0.5px; }
  .divider {
    position: absolute; left: 430px; top: 80px; bottom: 80px; width: 2px; background: var(--rule);
  }
  .details { position: absolute; left: 470px; top: 78px; }
  .person-name { font-family: "Libre Baskerville", serif; font-size: 34px; line-height: 1.1; font-weight: 400; }
  .person-title { font-family: "Libre Baskerville", serif; font-size: 18px; margin-top: 10px; color: var(--ink-soft); }
  .contact { list-style: none; margin-top: 26px; font-family: "Raleway", sans-serif; font-size: 21px; color: var(--ink); }
  .contact li { display: flex; align-items: center; height: 34px; white-space: nowrap; }
  .contact .icon { width: 22px; margin-right: 12px; display: inline-flex; justify-content: center; flex: none; }
  .contact .icon svg { width: 16px; height: 16px; fill: none; stroke: var(--ink); stroke-width: 1.6; }
</style>
</head>
<body>
<div class="stage">
  <div class="card">
    <div class="brand">
      <span class="brand-mark"></span>
      <span class="brand-name">Harlow Building<br>Partners, Inc.</span>
    </div>
    <div class="divider"></div>
    <div class="details">
      <h1 class="person-name">Martin Kessler</h1>
      <p class="person-title">President</p>
      <ul class="contact">
        <li><span class="icon"></span>48 Quarry Lane</li>
        <li><span class="icon"></span>Millbrook, NY 12545</li>
        <li><span class="icon"><svg viewBox="0 0 16 16"><path d="M4 1.5l2.5 3-1.5 1.5c.8 1.8 2.2 3.2 4 4l1.5-1.5 3 2.5-1.5 2.5C7 13 3 9 1.5 3z"/></svg></span>+003 5184-2790</li>
        <li><span class="icon"><svg viewBox="0 0 16 16"><rect x="1.5" y="3.5" width="13" height="9"/><path d="M1.5 3.5l6.5 5 6.5-5"/></svg></span>info@harlowbuilding.com</li>
        <li><span class="icon"><svg viewBox="0 0 16 16"><circle cx="8" cy="8" r="6.5"/><path d="M1.5 8h13M8 1.5c-3 3.5-3 9.5 0 13M8 1.5c3 3.5 3 9.5 0 13"/></svg></span>www.harlowbuilding.com</li>
        <li><span class="icon"></span>Contractor Lic. No. 204718</li>
      </ul>
    </div>
  </div>
</div>
</body>
</html>
```